KVT Business Cards

We require business cards for our business. We would like a matte black back to the card, with our logo centred in the middle. The front side of the card is open to design.

Target Market(s)

Clients looking for legal services (professional)

Industry/Entity Type

Legal

Contact Information for Business Card

Boris Telemark
Partner
Mobile: 0438 715 642
Email: boris@kvtlaw.co
Website: www.kvtlaw.co
Level 3, 118 Wexbury Street
Sydney NSW 2000

Font styles to use
Other font styles liked:
• Avenir

Colors
f04a50
ffffff
1b1b1b

Requirements
Must have
• Black back with logo included in the centre of the card.
• Our font is Avenir.

```html
<!DOCTYPE html>
<html lang="en">
<head>
<meta charset="utf-8">
<title>KVT Business Cards</title>
<link href="https://fonts.googleapis.com/css2?family=Nunito+Sans:wght@400;600;800&display=swap" rel="stylesheet">
<style>
  :root {
    --backdrop: #2a2a2a;
    --crimson: #c8213f;
    --ink: #1b1b1b;
    --ink-light: #262626;
    --paper: #ffffff;
    --muted: #444444;
    --rule: #cfcfcf;
  }
  html, body {
    margin: 0;
    padding: 0;
    width: 1200px;
    height: 892px;
    overflow: hidden;
    background: var(--backdrop);
    font-family: "Nunito Sans", Arial, sans-serif;
  }
  .canvas {
    position: relative;
    width: 1200px;
    height: 892px;
  }
  .card {
    position: absolute;
    width: 600px;
    height: 343px;
    box-shadow: 0 18px 40px rgba(0,0,0,0.55);
    overflow: hidden;
  }

  /* Back of card */
  .card-back {
    left: 60px;
    top: 70px;
    background: linear-gradient(135deg, var(--ink-light), var(--ink));
  }
  .card-back .brand {
    position: absolute;
    left: 0;
    right: 0;
    top: 138px;
    display: flex;
    justify-content: center;
    align-items: center;
    gap: 14px;
    color: var(--paper);
    font-weight: 800;
    font-size: 56px;
    line-height: 1;
    letter-spacing: 4px;
  }
  .card-back .brand-square {
    width: 18px;
    height: 18px;
    background: var(--crimson);
  }
  .card-back .web {
    position: absolute;
    right: 44px;
    bottom: 36px;
    color: var(--paper);
    font-size: 15px;
    letter-spacing: 9px;
  }

  /* Front of card */
  .card-front {
    left: 540px;
    top: 480px;
    background: var(--paper);
  }
  .card-front .brand {
    position: absolute;
    left: 40px;
    top: 86px;
    width: 240px;
    display: flex;
    align-items: flex-start;
    gap: 12px;
  }
  .card-front .brand-square {
    flex: none;
    width: 16px;
    height: 16px;
    margin-top: 5px;
    background: var(--crimson);
  }
  .card-front .brand-name {
    color: var(--ink);
    font-weight: 600;
    font-size: 21px;
    line-height: 1.05;
    text-transform: uppercase;
  }
  .card-front .divider {
    position: absolute;
    left: 292px;
    top: 36px;
    width: 1px;
    height: 150px;
    background: var(--rule);
  }
  .card-front .contact {
    position: absolute;
    left: 314px;
    top: 34px;
    color: var(--muted);
    font-size: 14px;
    line-height: 1.35;
  }
  .contact .person {
    color: var(--crimson);
    font-weight: 800;
    font-size: 22px;
    line-height: 1.1;
  }
  .contact .role {
    color: var(--ink);
    font-size: 15px;
    margin-bottom: 10px;
  }
  .contact .line {
    display: flex;
    align-items: center;
    gap: 8px;
  }
  .contact .line svg { flex: none; }
  .contact .address { margin-bottom: 6px; }

  .card-front .band-dark {
    position: absolute;
    left: 0;
    right: 0;
    top: 276px;
    height: 42px;
    background: var(--ink);
  }
  .card-front .band-accent {
    position: absolute;
    left: 190px;
    top: 258px;
    width: 380px;
    height: 40px;
    background: var(--crimson);
    clip-path: polygon(18px 0, 100% 0, calc(100% - 18px) 100%, 0 100%);
    display: flex;
    align-items: center;
    justify-content: center;
  }
  .card-front .web {
    color: var(--paper);
    font-size: 14px;
    letter-spacing: 8px;
    padding-left: 8px;
  }
</style>
</head>
<body>
<main class="canvas">

  <section class="card card-back" aria-label="Card back">
    <div class="brand">
      <span class="brand-square"></span>
      <span class="brand-name">KVT</span>
    </div>
    <div class="web">WWW.KVTLAW.CO</div>
  </section>

  <section class="card card-front" aria-label="Card front">
    <div class="brand">
      <span class="brand-square"></span>
      <span class="brand-name">Kovac Vance<br>Telemark<br>Legal</span>
    </div>

    <div class="divider"></div>

    <div class="contact">
      <div class="person">Boris Telemark</div>
      <div class="role">Partner</div>
      <div class="address">Level 3, 118 Wexbury Street<br>Sydney NSW 2000</div>
      <div class="line">
        <svg width="12" height="16" viewBox="0 0 12 16" aria-hidden="true">
          <rect x="1.5" y="1" width="9" height="14" rx="1.5" fill="none" stroke="#c8213f" stroke-width="1.8"/>
          <rect x="4.5" y="12" width="3" height="1.2" fill="#c8213f"/>
        </svg>
        <span>0438 715 642</span>
      </div>
      <div class="line">
        <svg width="14" height="10" viewBox="0 0 14 10" aria-hidden="true">
          <rect x="0" y="0" width="14" height="10" fill="#c8213f"/>
          <path d="M0 0 L7 6 L14 0" fill="none" stroke="#ffffff" stroke-width="1.2"/>
        </svg>
        <span>boris@kvtlaw.co</span>
      </div>
    </div>

    <div class="band-dark"></div>
    <div class="band-accent">
      <span class="web">WWW.KVTLAW.CO</span>
    </div>
  </section>

</main>
</body>
</html>
```